Business Card Design Project

KB Consulting Associates is a management consulting business with C-suite (CEO/CFO etc) target clients. Logo selected is blue with simple/serious typefaces.

Target Market(s)

CEOs and CFOs of large corporates

Industry/Entity Type

Management Consulting

Font styles to use
Serif

Colors
3276b5

Requirements
Must have
• Tag line: Building successful collaborations (use different font)
Address: 427 Fernvale Crescent #03-22 Singapore 519337
Telephone: +65 8372 4096
Email: kbloh@postnest42.com

```html
<!DOCTYPE html>
<html lang="en">
<head>
<meta charset="utf-8">
<title>KB Consulting Associates — Business Cards</title>
<link rel="stylesheet" href="https://fonts.googleapis.com/css2?family=Open+Sans:wght@400;600;700&display=swap">
<style>
  :root {
    --brand-blue: #3276b5;
    --deep-blue: #1f65a8;
    --ink: #1a1a1a;
    --muted: #555555;
    --card: #ffffff;
    --backdrop: #ececec;
    --rule: #3a3a3a;
  }
  * { box-sizing: border-box; margin: 0; padding: 0; }
  html, body {
    width: 1200px; height: 1001px; overflow: hidden;
    background: var(--backdrop);
    font-family: "Open Sans", Arial, sans-serif;
  }
  .sheet {
    position: relative; width: 1200px; height: 1001px;
    display: flex; align-items: center; justify-content: center; gap: 50px;
  }
  .card {
    position: relative; width: 525px; height: 300px;
    background: var(--card); overflow: hidden;
    box-shadow: 0 2px 10px rgba(0,0,0,0.12);
  }
  .wordmark {
    position: absolute; left: 40px; top: 38px;
    font-weight: 600; font-size: 26px; letter-spacing: 0.5px;
    color: var(--brand-blue); white-space: nowrap;
  }
  /* Front */
  .card--front .swoosh { position: absolute; inset: 0; width: 100%; height: 100%; }
  .person { position: absolute; left: 118px; top: 112px; text-align: center; }
  .person__name { font-weight: 700; font-size: 16px; color: var(--brand-blue); }
  .person__title { font-size: 9px; color: var(--muted); letter-spacing: 0.5px; }
  .contact {
    position: absolute; left: 262px; top: 160px;
    border-left: 1.5px solid var(--rule);
    padding-left: 16px; display: grid;
    grid-template-columns: 16px auto; column-gap: 10px; row-gap: 3px;
    font-size: 13.5px; color: var(--ink); line-height: 1.3;
  }
  .contact__icon { width: 14px; height: 14px; fill: var(--deep-blue); margin-top: 2px; }
  /* Back */
  .card--back .wordmark { left: 50px; top: 95px; font-size: 30px; }
  .tagline {
    position: absolute; left: 50px; top: 142px;
    font-size: 15px; color: var(--brand-blue); letter-spacing: 0.2px;
  }
  .card--back .base-band {
    position: absolute; left: 0; right: 0; bottom: 0; height: 10px;
    background: var(--brand-blue);
  }
</style>
</head>
<body>
<main class="sheet">
  <section class="card card--front" aria-label="Business card front">
    <svg class="swoosh" viewBox="0 0 525 300" preserveAspectRatio="none" aria-hidden="true">
      <path d="M0 120 C 70 150, 150 235, 300 300 L 0 300 Z" fill="#1a1a1a"/>
      <path d="M0 140 C 120 180, 260 250, 525 300 L 0 300 Z" fill="var(--deep-blue)"/>
      <path d="M0 150 C 120 190, 260 255, 525 300 L 525 300 L 0 300 Z" fill="#ffffff" opacity="0"/>
      <path d="M0 152 C 130 195, 280 262, 480 300 L 0 300 Z" fill="#ffffff"/>
    </svg>
    <div class="wordmark">KB Consulting Associates</div>
    <div class="person">
      <div class="person__name">Kaelin</div>
      <div class="person__title">CEO</div>
    </div>
    <div class="contact">
      <svg class="contact__icon" viewBox="0 0 16 16"><path d="M8 0a5.5 5.5 0 0 0-5.5 5.5C2.5 10 8 16 8 16s5.5-6 5.5-10.5A5.5 5.5 0 0 0 8 0zm0 8a2.5 2.5 0 1 1 0-5 2.5 2.5 0 0 1 0 5z"/></svg>
      <span>427 Fernvale Crescent<br>#03-22 Singapore 519337</span>
      <svg class="contact__icon" viewBox="0 0 16 16"><path d="M3.6 1.2l2.3 2.4-1.3 2a9 9 0 0 0 5.8 5.8l2-1.3 2.4 2.3-1.6 2.2C7 14.2 1.8 9 1.4 2.8z"/></svg>
      <span>+65 8372 4096</span>
      <svg class="contact__icon" viewBox="0 0 16 16"><path d="M1 3h14v10H1z M1 3l7 6 7-6" stroke="#fff" stroke-width="1"/></svg>
      <span>kbloh@postnest42.com</span>
    </div>
  </section>

  <section class="card card--back" aria-label="Business card back">
    <div class="wordmark">KB Consulting Associates</div>
    <p class="tagline">Building successful collaborations</p>
    <div class="base-band"></div>
  </section>
</main>
</body>
</html>
```